LBFC Business cards

We are an established dental practice that is looking for new business cards to match our new logo. We are looking for something unique and sophisticated.
BRIEF: Colours are black, silver and white. Include the company name, logo (including “Larkspur Bend Family Care”) and phone number “03 9416 2857”.
Front - Include the company name, logo (including “Larkspur Bend Family Care”) and phone number “03 9416 2857”.
Back - Include the company name,  “Larkspur Bend Family Care”, phone number “03 9416 2857”. address "84C Tilbury Street, Larkspur Bend, Vic 3187", "Email reception@larkspurbendfamilycare.com.au", the Dentist Name " Dr ................................"  Your next appointment "Day, date and time(am/pm)".  3 lines for 3 appointments please, and at the bottom "IF UNABLE TO KEEP THIS APPOINTMENT 48 HOURS NOTICE IS REQUIRED."
Try and be creative and different with the design, i've added an image for inspiration

Target Market(s)
ALL in need of dental
Industry/Entity Type
Dental Clinic

```html
<!DOCTYPE html>
<html lang="en">
<head>
<meta charset="utf-8">
<title>LBFC Business Cards</title>
<link rel="stylesheet" href="https://fonts.googleapis.com/css2?family=Montserrat:wght@500;700&family=Roboto:wght@400;500;700&display=swap">
<style>
  :root {
    --backdrop: #3b3b3d;
    --card-white: #ffffff;
    --card-black: #151516;
    --ink: #1c1c1c;
    --silver: #c9c9cc;
    --silver-soft: #ececee;
    --dot: #555555;
  }
  * { box-sizing: border-box; margin: 0; padding: 0; }
  html, body {
    width: 1200px; height: 801px; overflow: hidden;
    background: var(--backdrop);
  }
  .stage {
    width: 1200px; height: 801px;
    display: flex; align-items: center; justify-content: center; gap: 48px;
  }
  .card {
    position: relative;
    width: 520px; height: 316px;
    overflow: hidden;
    box-shadow: 0 10px 28px rgba(0,0,0,.45);
  }

  /* Appointment side */
  .card--appointment { background: var(--card-white); color: var(--ink); font-family: "Roboto", sans-serif; }
  .watermark-ring {
    position: absolute; left: 230px; top: 18px;
    width: 230px; height: 230px; border-radius: 50%;
    border: 22px solid var(--silver-soft);
  }
  .card-header {
    position: absolute; left: 26px; top: 24px; right: 26px;
    display: flex; align-items: flex-start; gap: 10px;
  }
  .brand { font-family: "Montserrat", sans-serif; line-height: 1; }
  .brand__name { font-weight: 700; font-size: 19px; letter-spacing: .5px; }
  .brand__sub { font-weight: 500; font-size: 9.5px; letter-spacing: 2.4px; margin-top: 3px; white-space: nowrap; }
  .header-divider { width: 1px; height: 34px; background: var(--ink); }
  .contact { font-size: 10.5px; line-height: 1.45; }

  .field { display: flex; align-items: flex-end; font-size: 12px; }
  .field__fill { flex: 1; border-bottom: 1.5px dotted var(--dot); margin: 0 4px 3px; }
  .dentist { position: absolute; left: 26px; top: 82px; width: 470px; }

  .appointment-title {
    position: absolute; left: 0; right: 0; top: 112px; text-align: center;
    font-size: 12.5px; font-weight: 700; letter-spacing: .8px;
  }
  .appointment-title::after {
    content: ""; display: block; width: 200px; height: 1.5px; background: var(--ink);
    margin: 6px auto 0;
  }
  .appointment-rows { position: absolute; left: 26px; top: 152px; width: 470px; display: grid; gap: 14px; }
  .appointment-row { display: flex; gap: 6px; }
  .appointment-row .field:first-child { flex: 1.15; }
  .appointment-row .field:nth-child(2) { flex: 1; }

  .notice-band {
    position: absolute; left: 0; right: 0; bottom: 0; height: 34px;
    background: var(--card-black); color: #f2f2f2;
    display: flex; align-items: center; justify-content: center;
    font-size: 10.5px; letter-spacing: .6px;
  }
  .notice-band strong { font-weight: 700; margin: 0 4px; }

  /* Brand side */
  .card--brand { background: linear-gradient(160deg, #1e1e20 0%, var(--card-black) 60%, #0d0d0e 100%); color: #ffffff; }
  .brand-ring {
    position: absolute; left: 40px; top: 40px;
    width: 250px; height: 250px; border-radius: 50%;
    border: 18px solid #232325;
  }
  .brand--front { position: absolute; right: 30px; bottom: 52px; }
  .brand--front .brand__name { font-size: 22px; }
  .brand--front .brand__sub { font-size: 10.5px; color: var(--silver); }
</style>
</head>
<body>
<main class="stage">
  <section class="card card--appointment" aria-label="Appointment side">
    <div class="watermark-ring"></div>
    <header class="card-header">
      <div class="brand">
        <div class="brand__name">LARKSPUR BEND</div>
        <div class="brand__sub">FAMILY CARE— 03 9416 2857</div>
      </div>
      <div class="header-divider"></div>
      <div class="contact">
        <div>84C Tilbury Street, Larkspur Bend, Vic 3187</div>
        <div>reception@larkspurbendfamilycare.com.au</div>
      </div>
    </header>
    <div class="field dentist"><span>Dr</span><span class="field__fill"></span></div>
    <h2 class="appointment-title">YOUR NEXT APPOINTMENT</h2>
    <div class="appointment-rows">
      <div class="appointment-row">
        <div class="field"><span>Date</span><span class="field__fill"></span></div>
        <div class="field"><span>Time</span><span class="field__fill"></span><span>am/pm</span></div>
      </div>
      <div class="appointment-row">
        <div class="field"><span>Date</span><span class="field__fill"></span></div>
        <div class="field"><span>Time</span><span class="field__fill"></span><span>am/pm</span></div>
      </div>
      <div class="appointment-row">
        <div class="field"><span>Date</span><span class="field__fill"></span></div>
        <div class="field"><span>Time</span><span class="field__fill"></span><span>am/pm</span></div>
      </div>
    </div>
    <footer class="notice-band">IF UNABLE TO KEEP THIS APPOINTMENT <strong>48</strong> HOURS NOTICE IS REQUIRED.</footer>
  </section>

  <section class="card card--brand" aria-label="Brand side">
    <div class="brand-ring"></div>
    <div class="brand brand--front">
      <div class="brand__name">LARKSPUR BEND</div>
      <div class="brand__sub">FAMILY CARE— 03 9416 2857</div>
    </div>
  </section>
</main>
</body>
</html>
```